Harbor of Bright Morning Paths, LLC needs business stationary designed using our logo.

Harbor of Bright Morning Paths is a new life coaching business. We have a logo design . We need a design for stationary for branding a new PathCrafter Life Coach business. We help people transform their lives by exploring, designing and taking action steps for the life they love in the areas of health and wellness, relationships, vocation, and time and money freedom. We like bright happy colors that present growth and transformation and also compliments the blue logo design.

Hello Designers, Thank you for accepting my design request. I wanted to be sure I put all the information for the business stationary design. If this is already in the order please disregard. Information to incorporate into stationary design Logo: incorporate blues and complimentary color Company name: Harbor of Bright Morning Paths, LLC Tagline: Transformational Life Coaching "If you can think it, you can do it You CAN live a life you LOVE! Website: www.norasaltwell.PathCrafterGuide.com Email: norasaltwell@PathCrafterGuide.com P.O. Box 5293 Edcouch, TX 78538 555-017-392 Nora T. Saltwell, Certified PathCrafter* Coach Positive, upbeat, professional design Thank you.

Industry/Entity Type

Life Coaching

Font styles to use
Decorative

Colors
0355a3

Requirements
Must have
• Information to incorporate into stationary design
• Logo: incorporate blues and complimentary color
• Company name: Harbor of Bright Morning Paths, LLC
• Tagline: Transformational Life Coaching
• "If you can think it, you can do it You CAN live a life you LOVE!
• Website: www.norasaltwell.PathCrafterGuide.com
• Email: norasaltwell@PathCrafterGuide.com
• P.O. Box 5293 Edcouch, TX 78538 555-017-392
• Nora T. Saltwell, Certified PathCrafter* Coach
• Positive, upbeat, professional design
Nice to have
• Watermark
Should not have
• No negativity or negative vibes
• Nothing derogatory
• No clashing colors

```html
<!DOCTYPE html>
<html lang="en">
<head>
<meta charset="utf-8">
<title>Harbor of Bright Morning Paths — Stationery</title>
<link rel="stylesheet" href="https://fonts.googleapis.com/css2?family=Montserrat:wght@300;400;800&family=Arimo:wght@400;700&family=Dancing+Script:wght@600&display=swap">
<style>
:root{
  --stage:#2c2c2c;
  --paper:#ffffff;
  --purple:#652e91;
  --purple-deep:#5d2a8e;
  --blue:#3b4aa6;
  --brand:#4b34a3;
  --ink:#222222;
  --muted:#555555;
  --rule:#5a3f9e;
  --wash:#ebe8f4;
  --white:#ffffff;
}
*{margin:0;padding:0;box-sizing:border-box}
html,body{width:1189px;height:1200px;overflow:hidden;background:var(--stage)}
.canvas{position:relative;width:1189px;height:1200px;background:var(--stage)}
.piece{position:absolute;overflow:hidden}
.abs{position:absolute;white-space:nowrap}
.brand-name{font-family:"Montserrat",sans-serif;font-weight:800;color:var(--brand)}
.brand-sub{font-family:"Montserrat",sans-serif;font-weight:300;color:var(--muted)}
.mark{position:absolute;border-radius:50%;background:var(--brand)}
.wash{position:absolute;border-radius:50%;background:var(--wash)}
.contact{font-family:"Montserrat",sans-serif;font-weight:400;color:var(--muted);font-size:7px;line-height:8.5px}
.contact .ico{display:inline-block;width:6px;height:6px;border-radius:50%;background:var(--brand);margin-right:3px;vertical-align:-0.5px}
.url{font-family:"Montserrat",sans-serif;font-weight:400;color:var(--muted);letter-spacing:2px}
.rule{position:absolute;height:1px;background:var(--rule)}
.band{position:absolute;left:0;right:0;bottom:0;background:var(--purple)}

/* purple covers */
.cover{background:radial-gradient(circle at 29% 67%, var(--blue) 0%, #4c3aa0 28%, var(--purple) 62%, var(--purple-deep) 100%)}
.cover .brand-name{color:var(--white)}
.cover .brand-sub{color:#e5ddf2}
.cover .glow{position:absolute;border-radius:50%;background:rgba(255,255,255,.06)}
.motto{font-family:"Montserrat",sans-serif;font-weight:400;color:var(--white);letter-spacing:.8px}

/* folder */
.folder{left:120px;top:70px;width:449px;height:580px}
.folder .spine{position:absolute;left:17px;top:0;bottom:0;width:3px;background:rgba(255,255,255,.12)}

/* letterhead */
.letterhead{left:622px;top:73px;width:447px;height:578px;background:var(--paper)}
.letter-body{position:absolute;left:163px;top:142px;width:246px;font-family:"Arimo",sans-serif;font-size:7.4px;line-height:13px;color:var(--ink)}
.letter-body p{margin-bottom:7px}
.signoff{position:absolute;left:163px;top:451px;font-family:"Arimo",sans-serif;font-size:8px;color:var(--ink)}
.signature{position:absolute;left:162px;top:471px;font-family:"Dancing Script",cursive;font-size:27px;color:var(--ink)}
.signer{position:absolute;left:163px;top:509px;font-family:"Arimo",sans-serif;font-size:8.5px;line-height:10.5px;color:var(--ink)}
.signer b{font-weight:700}

/* envelope */
.envelope-front{left:120px;top:691px;width:404px;height:202px;background:var(--paper)}
.envelope-back{left:120px;top:926px;width:404px;height:202px;background:var(--paper)}
.flap{position:absolute;left:0;top:0;width:404px;height:64px}

/* business cards */
.card-front{left:565px;top:792px;width:270px;height:154px;background:var(--paper)}
.card-back{left:566px;top:975px;width:269px;height:153px}
.person{font-family:"Montserrat",sans-serif;font-weight:400;color:var(--brand)}

/* notebook */
.notebook{left:869px;top:850px;width:200px;height:277px;border-left:4px solid #d8d4e4}
</style>
</head>
<body>
<main class="canvas">

  <section class="piece folder cover" aria-label="Presentation folder cover">
    <div class="spine"></div>
    <div class="glow" style="left:-60px;top:250px;width:260px;height:260px"></div>
    <div class="abs brand-name" style="left:0;width:449px;text-align:center;top:76px;font-size:10.5px">Harbor of Bright Morning Paths, LLC</div>
    <div class="abs brand-sub" style="left:0;width:449px;text-align:center;top:88px;font-size:8px">Transformational Coaching</div>
    <div class="abs motto" style="left:0;width:449px;text-align:center;top:546px;font-size:7.4px">If you can think it, you can do it You CAN live a life you LOVE</div>
  </section>

  <section class="piece letterhead" aria-label="Letterhead">
    <div class="wash" style="left:-2px;top:295px;width:212px;height:212px"></div>
    <div class="mark" style="left:285px;top:29px;width:38px;height:38px"></div>
    <div class="abs brand-name" style="right:38px;top:82px;font-size:10px">Harbor of Bright Morning Paths, LLC</div>
    <div class="abs brand-sub" style="right:96px;top:94px;font-size:7.5px">Transformational Coaching</div>

    <div class="abs contact" style="left:36px;top:104px">
      <div><span class="ico"></span>norasaltwell@PathCrafterGuide.com</div>
      <div><span class="ico"></span>555-017-392</div>
    </div>
    <div class="rule" style="left:36px;top:128px;width:88px"></div>
    <div class="abs contact" style="left:36px;top:132px">
      <div>P.O. Box 5293 Fernhollow,</div>
      <div>TX 79990</div>
    </div>

    <div class="letter-body">
      <p>electronic typesetting, remaining essentially unchanged. It was popularised with the release of Linotrace sheets containing Lorem Ipsum passages, and more recently with Alder PageSetter including versions of Lorem Ipsum.</p>
      <p>It is a long established fact that a reader will be distracted by the readable content of a page when looking at its layout. The point of using Lorem Ipsum is that it has a more-or-less normal distribution of letters, as opposed to using 'Content here, content here', making it look like readable English. Many desktop publishing packages and web page editors now use Lorem Ipsum as their default model text, and a search for 'lorem ipsum' will uncover many web sites still in their infancy. Various versions have evolved over the years.</p>
      <p>Lorem Ipsum is simply dummy text of the printing and typesetting industry. Lorem Ipsum has been the industry's standard dummy text ever since the 1500s, when an unknown printer scrambled it to make a type specimen book. It has survived not only five centuries, but also the leap into electronic typesetting, remaining essentially unchanged.</p>
      <p>It is a long established fact that a reader will be distracted by the readable content of a page when looking at its layout. The point of using Lorem Ipsum is that it has a more-or-less normal distribution.</p>
    </div>
    <div class="signoff">Regards,</div>
    <div class="signature">Elsa Marrow</div>
    <div class="signer"><b>Elsa Marrow</b><br>General Maneger</div>

    <div class="rule" style="left:36px;top:548px;width:375px"></div>
    <div class="abs url" style="left:36px;width:375px;text-align:center;top:552px;font-size:7px">www.norasaltwell.PathCrafterGuide.com</div>
    <div class="band" style="height:8px"></div>
  </section>

  <section class="piece envelope-front" aria-label="Envelope front">
    <div class="wash" style="left:212px;top:0;width:196px;height:196px"></div>
    <div class="mark" style="left:92px;top:21px;width:32px;height:32px"></div>
    <div class="abs brand-name" style="left:43px;top:57px;font-size:8.6px">Harbor of Bright Morning Paths, LLC</div>
    <div class="abs brand-sub" style="left:68px;top:67px;font-size:6.5px">Transformational Coaching</div>
    <div class="abs contact" style="left:43px;top:141px">
      <div>P.O. Box 5293 Fernhollow,</div>
      <div>TX 79990</div>
      <div><span class="ico"></span>norasaltwell@PathCrafterGuide.com</div>
      <div><span class="ico"></span>555-017-392</div>
    </div>
    <div class="rule" style="left:43px;top:182px;width:337px"></div>
    <div class="abs url" style="right:25px;top:185px;font-size:6.6px">www.norasaltwell.PathCrafterGuide.com</div>
    <div class="band" style="height:5px"></div>
  </section>

  <section class="piece envelope-back" aria-label="Envelope back">
    <svg class="flap" viewBox="0 0 404 64" aria-hidden="true">
      <defs>
        <radialGradient id="flapGlow" cx="50%" cy="45%" r="55%">
          <stop offset="0%" stop-color="#3b4aa6"/>
          <stop offset="55%" stop-color="#652e91"/>
          <stop offset="100%" stop-color="#5d2a8e"/>
        </radialGradient>
      </defs>
      <path d="M0 0 H404 V38 Q404 48 396 60 Q394 63 388 63 H16 Q10 63 8 60 Q0 48 0 38 Z" fill="url(#flapGlow)"/>
    </svg>
    <div class="abs brand-name" style="left:0;width:404px;text-align:center;top:22px;font-size:7px;color:var(--white)">Harbor of Bright Morning Paths, LLC</div>
    <div class="abs brand-sub" style="left:0;width:404px;text-align:center;top:31px;font-size:5px;color:#e5ddf2">Transformational Coaching</div>
  </section>

  <section class="piece card-front" aria-label="Business card front">
    <div class="wash" style="left:-14px;top:30px;width:110px;height:110px"></div>
    <div class="mark" style="left:118px;top:22px;width:30px;height:30px"></div>
    <div class="abs brand-name" style="left:0;width:270px;text-align:center;top:53px;font-size:7.4px">Harbor of Bright Morning Paths, LLC</div>
    <div class="abs brand-sub" style="left:0;width:270px;text-align:center;top:62px;font-size:5.6px">Transformational Coaching</div>
    <div class="abs person" style="left:0;width:270px;text-align:center;top:75px;font-size:8.5px">Nora T. Saltwell</div>
    <div class="abs brand-sub" style="left:0;width:270px;text-align:center;top:86px;font-size:6px">Certified PathCrafter | Coach</div>
    <div class="abs contact" style="left:0;width:270px;text-align:center;top:99px;font-size:7px;line-height:9px">
      <div>norasaltwell@PathCrafterGuide.com</div>
      <div>555-017-392</div>
      <div>P.O. Box 5293 Fernhollow, TX 79990</div>
    </div>
    <div class="rule" style="left:26px;top:134px;width:216px"></div>
    <div class="abs url" style="left:0;width:270px;text-align:center;top:137px;font-size:6px;letter-spacing:1.2px">www.norasaltwell.PathCrafterGuide.com</div>
    <div class="band" style="height:5px"></div>
  </section>

  <section class="piece card-back cover" aria-label="Business card back">
    <div class="glow" style="left:-20px;top:30px;width:110px;height:110px"></div>
    <div class="abs motto" style="left:0;width:269px;text-align:center;top:59px;font-size:10px;line-height:13px;white-space:normal">If you can think it<br>you can do it You CAN live a life you LOVE</div>
  </section>

  <section class="piece notebook cover" aria-label="Notebook cover">
    <div class="glow" style="left:-30px;top:120px;width:140px;height:140px"></div>
    <div class="abs brand-name" style="left:0;width:196px;text-align:center;top:34px;font-size:5.4px">Harbor of Bright Morning Paths, LLC</div>
    <div class="abs brand-sub" style="left:0;width:196px;text-align:center;top:41px;font-size:3.8px">Transformational Coaching</div>
    <div class="abs motto" style="left:0;width:196px;text-align:center;top:261px;font-size:3.4px;letter-spacing:.2px">If you can think it, you can do it You CAN live a life you LOVE</div>
  </section>

</main>
</body>
</html>
```